Law Firm Web Design Project

I need a website design for my law firm. I have attached to this description the URL of a website I liked with a description of the elements of that website that appeal to me.

I am also attaching my law firm's logo, so you can review that design when you create the website design.

Reference Site: www.harborfamilycounselpros.com

What we like about this site:
• The different layers
• Subtle designs, textures, curves
• 3 dimensional
• Floating effect
• Simple logo that stands out (we are providing logo)
• Prominent phone number
• Location of Areas of Practice
oDivorce, Legal Separation, Paternity, Spousal Maintenance, Child Custody, Child Support, Protective Orders, Community Property, Business Evaluations
• The limited amount of links across the top
o Home, Meet Our Attorney, FAQ, Contact Us
• Request A Consultation click through
• Right side bar with the moving icons
• Badges

Other Tips:
• We don’t want the website to be dark. The logo can standout and the website can have its own colors and flow.
• We would like there to be a “call to action” or way to get in touch on every page and every page view
• We would like a place for credit card icons at the bottom of the page
• Strong, yet elegant
• Finally, just use the website provided as a guide. Explore different colors, textures, shapes, shadows etc.
Updates

I would prefer the website have colors that are complementary to my logo and that are strong and elegant.  I like black, gold, amber, and tan colors.  Black should be used sparingly as an accent only, since I don't want the website to be too dark.

Please review the website I provided as an example in my project description.  I really like the three dimensional aspects of that website (web page floating on top of a background and the logo in the upper left floating on top of the web page).  I also like the use of "swirling" on the background and the webpage.  I hope this additional information is helpful.

Requirements
Must have
• I need a place to insert "client testimonials", a place to insert four logos of awards the law firm has received, a place for people to fill out a form to contact the law firm via email, and a place for people to click to review articles I have written.

```html
<!DOCTYPE html>
<html lang="en">
<head>
<meta charset="utf-8">
<title>Whitcombe Law</title>
<link href="https://fonts.googleapis.com/css2?family=PT+Serif:ital,wght@0,400;0,700;1,400&family=Open+Sans:wght@400;600&family=Arimo&display=swap" rel="stylesheet">
<style>
:root{
  --backdrop-dark:#8a6a45;
  --backdrop-light:#d2b48c;
  --gold:#b8892f;
  --gold-light:#d4a94a;
  --gold-text:#9c8a3c;
  --tab:#8c9ea3;
  --tab-dark:#7b8d92;
  --beige:#e6ddc3;
  --cream:#f3efe3;
  --text:#5c5c5c;
  --title:#6c6c6c;
  --footer-top:#4a4a4a;
  --footer-bottom:#111;
  --white:#fff;
}
*{box-sizing:border-box;margin:0;padding:0}
html,body{width:1044px;height:1200px;overflow:hidden}
body{position:relative;font-family:"Open Sans",sans-serif;color:var(--text)}
.backdrop{
  position:absolute;inset:0;
  background:
    radial-gradient(ellipse at 8% 30%,rgba(255,230,190,.35),transparent 40%),
    radial-gradient(ellipse at 92% 30%,rgba(255,230,190,.35),transparent 40%),
    linear-gradient(90deg,var(--backdrop-dark),var(--backdrop-light) 8%,var(--backdrop-dark) 15%,var(--backdrop-light) 85%,var(--backdrop-dark));
}
.page{position:absolute;left:154px;top:0;width:737px;height:1200px;background:var(--white);box-shadow:0 0 14px rgba(0,0,0,.45);overflow:hidden}
.abs{position:absolute}

/* header */
.header{left:0;top:0;width:737px;height:124px;background:linear-gradient(120deg,#f1ead8,#e7dcc2)}
.header-sheen{left:290px;top:0;width:447px;height:95px;background:linear-gradient(180deg,#fff,#f4f0e8 70%,#e9e3d6);border-bottom-left-radius:60px 95px}
.brand{left:28px;top:40px;display:flex;align-items:center;gap:12px}
.brand-mark{width:34px;height:34px;background:#1c1c1c}
.brand-name{font-family:"PT Serif",serif;font-size:29px;color:var(--gold-text);line-height:1;white-space:nowrap}
.call{left:416px;top:28px;font-family:"Arimo",sans-serif;color:#888;font-size:12px;white-space:nowrap}
.call strong{font-weight:400;font-size:24px;color:#555;margin-left:4px;vertical-align:-2px}
.nav{left:333px;top:92px;width:404px;height:32px;background:linear-gradient(#9aa8ac,#7f9196);border-top-left-radius:28px 32px;display:flex;align-items:center;justify-content:flex-end;padding-right:4px}
.nav a{font-family:"PT Serif",serif;font-size:13px;line-height:16px;color:var(--white);text-decoration:none;padding:0 11px;border-left:1px solid rgba(255,255,255,.35);white-space:nowrap}
.nav a:first-child{border-left:none;color:#e7c98a}

/* hero */
.hero{left:0;top:124px;width:737px;height:346px;background:linear-gradient(180deg,#6f8a82 0%,#9bab9e 30%,#d8c7a8 62%,#e6d6bb 100%)}
.consult-tab{left:3px;top:287px;width:24px;height:179px;background:rgba(255,255,255,.45)}
.consult-tab span{position:absolute;left:50%;top:50%;transform:translate(-50%,-50%) rotate(-90deg);white-space:nowrap;font-size:11px;color:#555;font-family:"Arimo",sans-serif}
.slide-card{left:427px;top:320px;width:224px;height:120px;background:rgba(243,236,222,.88);border-radius:6px;padding:10px 24px;box-shadow:0 2px 6px rgba(0,0,0,.2)}
.slide-card h2{font-family:"PT Serif",serif;font-weight:400;font-size:27px;color:#222;line-height:1.1}
.slide-card p{font-family:"PT Serif",serif;font-size:11px;color:#444;line-height:17px;margin-top:4px;white-space:nowrap}
.slide-cta{left:439px;top:405px;width:199px;height:27px;background:linear-gradient(#c99a3a,#a8782a);color:var(--white);font-family:"PT Serif",serif;font-size:15px;text-align:center;line-height:27px}
.dots{left:97px;top:444px;display:flex;gap:5px}
.dots i{width:13px;height:13px;border-radius:50%;background:var(--white);border:1px solid #bbb}
.dots i:first-child{background:#a08660}
.social{left:703px;top:322px;width:34px;height:148px;background:rgba(240,232,215,.55)}
.social i{position:absolute;left:5px;width:24px;height:24px;border-radius:4px;background:var(--cream);border:1px solid #d7c9a6}
.hero-rule{left:0;top:470px;width:737px;height:6px;background:linear-gradient(#4a4a4a,#8a8a8a)}

/* body columns */
.centre{left:190px;top:476px;width:385px;height:590px;background:var(--beige);border-top-left-radius:46px 60px;box-shadow:-2px 0 4px rgba(0,0,0,.12)}
.tab{height:29px;background:linear-gradient(#9aabb0,var(--tab-dark));color:var(--white);font-size:12px;line-height:29px;letter-spacing:.3px;text-transform:uppercase;font-family:"PT Serif",serif;white-space:nowrap}
.tab-left{left:0;width:174px;padding-left:20px;border-top-right-radius:6px}
.tab-right{left:577px;width:160px;padding-left:22px;border-top-left-radius:6px}
.small{font-size:9px;line-height:15px;color:#666}

.video{left:17px;top:546px;width:158px;height:120px;background:#000;border-radius:4px 4px 0 0}
.video-play{left:72px;top:48px;width:30px;height:30px;border-radius:50%;background:#777}
.video-bar{left:0;bottom:0;width:158px;height:10px;background:linear-gradient(#ddd,#aaa)}

.articles{left:2px;top:720px;width:172px;border:1px solid #ccc}
.articles li{list-style:none;height:23.5px;line-height:23px;padding-left:20px;font-size:9px;color:#666;border-top:1px solid #ccc;white-space:nowrap}
.articles li:first-child{border-top:none}
.articles li.active{background:var(--tab);color:#333}
.read-all{left:0;top:823px;width:170px;text-align:right;font-family:"PT Serif",serif;font-size:10px;color:#555}

.quote{left:10px;top:898px;width:176px;font-family:"PT Serif",serif;font-style:italic;font-size:10.5px;line-height:15.5px;letter-spacing:.3px;color:#555;padding-left:22px}
.quote::before{content:"\201C";position:absolute;left:2px;top:-4px;font-size:26px;line-height:26px;font-style:normal;color:#444}
.quote-author{left:30px;top:966px;font-family:"PT Serif",serif;font-size:10px;color:#555}
.divider{left:3px;top:991px;width:172px;height:1px;background:#ccc}
.accept{left:22px;top:1003px;font-family:"PT Serif",serif;font-size:10px;font-weight:700;color:#444}
.cards{left:23px;top:1020px;display:flex;gap:3px}
.cards i{width:37px;height:22px;border-radius:2px;background:#cfcfcf}
.cards i:nth-child(1){background:#7aa4c8}
.cards i:nth-child(2){background:#8a9bc4}
.cards i:nth-child(3){background:#d9a05a}
.cards i:nth-child(4){background:#e8e2d6}

/* centre content */
.welcome{left:228px;top:508px;width:345px}
.welcome h1{font-family:"PT Serif",serif;font-weight:400;font-size:25px;color:var(--title);margin-bottom:10px;white-space:nowrap}
.welcome p{font-size:10.6px;line-height:20px;letter-spacing:.4px;color:#5c5c5c;margin-bottom:19px}
.welcome ul{margin:0 0 19px 0;padding:0}
.welcome li{list-style:none;font-size:10.6px;line-height:20px;letter-spacing:.4px;padding-left:16px;position:relative}
.welcome li::before{content:"";position:absolute;left:3px;top:7px;width:6px;height:6px;border-radius:50%;background:#d6302a}
.centre-rule{left:228px;top:943px;width:340px;height:1px;background:linear-gradient(90deg,#c8bc9c,transparent)}
.badge{background:#c9c2b0;border-radius:3px}

/* right column */
.practice{left:577px;top:516px;width:150px;text-align:right}
.practice li{list-style:none;font-size:8.5px;line-height:17.4px;color:#555;white-space:nowrap}
.qc-desc{left:589px;top:715px;width:140px}
.field{left:588px;width:135px;height:19px;border:1px solid #ccc;border-radius:3px;background:var(--white);font-size:9px;color:#777;padding:3px 10px}
.field.area{height:67px}
.btn{left:655px;width:68px;height:19px;background:linear-gradient(#cfa041,#a9792a);color:var(--white);border-radius:3px;font-weight:600;font-size:11px;text-align:center;line-height:19px;font-family:"Arimo",sans-serif}

/* footer */
.footer{left:0;top:1066px;width:737px;height:134px;background:linear-gradient(var(--footer-top),var(--footer-bottom))}
.footer-links{left:31px;top:21px;font-size:8px;color:#ccc;white-space:nowrap}
.footer-links span{margin:0 4px;color:#999}
.footer-copy{left:31px;top:45px;width:480px;font-family:"PT Serif",serif;font-size:9px;line-height:13px;color:#c9ad5c}
.footer-rule{left:0;top:84px;width:500px;height:1px;background:linear-gradient(90deg,#666,transparent)}
.copyright{left:31px;top:97px;font-size:8px;color:#ccc;white-space:nowrap}
.footer-brand{left:528px;top:18px;display:flex;align-items:center;gap:10px}
.footer-brand .brand-mark{width:24px;height:24px;background:#000;border:1px solid #555}
.footer-brand .brand-name{font-size:23px}
.footer-phone{left:534px;top:60px;width:160px;text-align:center;font-family:"Arimo",sans-serif;font-size:21px;color:#ddd}
.footer-addr{left:534px;top:87px;width:160px;text-align:center;font-family:"PT Serif",serif;font-size:8px;line-height:11px;color:#ccc}
</style>
</head>
<body>
<div class="backdrop" role="img" aria-label="Soft draped tan fabric backdrop"></div>

<div class="page">
  <header>
    <div class="abs header"></div>
    <div class="abs header-sheen"></div>
    <div class="abs brand"><i class="brand-mark"></i><span class="brand-name">Whitcombe Law</span></div>
    <div class="abs call">Call Today: <strong>555.014.2863</strong></div>
    <nav class="abs nav">
      <a href="#">Home</a><a href="#">Meet our Attorneys</a><a href="#">Why Whitcombe</a><a href="#">Contact</a>
    </nav>
  </header>

  <section class="abs hero" role="img" aria-label="Photo of a smiling family walking barefoot along a beach by the sea"></section>
  <div class="abs consult-tab"><span>Request Free Consultation</span></div>
  <div class="abs slide-card">
    <h2>Lorem Ipsum</h2>
    <p>Praesent justo dolor,<br>lobortis quis, lobortis dignissim.</p>
  </div>
  <div class="abs slide-cta">Consult Us Now!</div>
  <div class="abs dots"><i></i><i></i><i></i><i></i></div>
  <div class="abs social" aria-label="Social links">
    <i style="top:15px"></i><i style="top:43px"></i><i style="top:74px"></i><i style="top:103px"></i>
  </div>
  <div class="abs hero-rule"></div>

  <div class="abs centre"></div>

  <!-- left column -->
  <div class="abs tab tab-left" style="top:476px">Video Center</div>
  <p class="abs small" style="left:20px;top:511px;width:160px">Aliquam congue fermentum nisl. aliar Mauris accumsan nulla vel diam.</p>
  <div class="abs video" role="img" aria-label="Video player">
    <div class="abs video-play"></div>
    <div class="abs video-bar"></div>
  </div>

  <div class="abs tab tab-left" style="top:687px">Read Recent Articles</div>
  <ul class="abs articles">
    <li>Aliquam congue fermentum nisl.</li>
    <li class="active">Mauris accumsan nulla vel diam.</li>
    <li>Aliquam congue fermentum nisl.</li>
    <li>Mauris accumsan nulla vel diam.</li>
  </ul>
  <div class="abs read-all">Read All &gt;&gt;</div>

  <div class="abs tab tab-left" style="top:855px">Clients Testimonials</div>
  <blockquote class="abs quote">Aliquam congue fermentum nisl. Mauris accumsan nulla vel diam. Sed in lacus ut enim adipiscing aliquet. &#8221;</blockquote>
  <div class="abs quote-author">--Owen Marsh</div>
  <div class="abs divider"></div>
  <div class="abs accept">We proudly accept</div>
  <div class="abs cards" aria-label="Accepted cards"><i></i><i></i><i></i><i></i></div>

  <!-- centre column -->
  <article class="abs welcome">
    <h1>Welcome to Whitcombe</h1>
    <p>Aliquam congue fermentum nisl. Mauris accumsan nulla vel diam. Sed in lacus ut enim adipiscing aliquet.</p>
    <p>Nulla venenatis. In pede mi, aliquet sit amet, euismod in, auctor ut, ligula. Aliquam dapibus tincidunt metus. Praesent justo dolor, lobortis quis, lobortis dignissim, pulvinar ac, lorem. Vestibulum sed ante. Donec sagittis euismod purus.</p>
    <ul>
      <li>Praesent justo dolor</li>
      <li>Donec sagittis euismod purus</li>
      <li>Mauris accumsan nulla vel diam</li>
    </ul>
    <p>Aliquam congue fermentum nisl. Mauris accumsan nulla vel diam. Sed in lacus ut enim adipiscing aliquet.</p>
    <p>Nulla venenatis. In pede mi, aliquet sit amet, euismod in, auctor ut, ligula. Aliquam dapibus tincidunt metus. Praesent justo dolor, lobortis quis, lobortis dignissim, pulvinar ac, lorem. Vestibulum sed ante. Donec sagittis euismod purus.</p>
  </article>
  <div class="abs centre-rule"></div>
  <div class="abs badge" style="left:216px;top:976px;width:100px;height:66px" aria-label="Award badge"></div>
  <div class="abs badge" style="left:341px;top:977px;width:65px;height:67px;border-radius:4px" aria-label="Accreditation badge"></div>
  <div class="abs badge" style="left:411px;top:978px;width:130px;height:64px" aria-label="Peer review badge"></div>

  <!-- right column -->
  <div class="abs tab tab-right" style="top:478px">Areas of Practice</div>
  <ul class="abs practice">
    <li>Divorce</li><li>Legal Separation</li><li>Paternity</li><li>Spousal Maintenance</li><li>Child Custody</li>
    <li>Child Support</li><li>Protective Orders</li><li>Community Property</li><li>Business Evaluations</li>
  </ul>

  <div class="abs tab tab-right" style="top:681px;padding-left:48px">Quick Contact</div>
  <p class="abs small qc-desc">Aliquam congue fermentum nisl. Mauris accumsan nulla vel diam.</p>
  <div class="abs field" style="top:748px">Name</div>
  <div class="abs field" style="top:771px">Phone</div>
  <div class="abs field" style="top:793px">Email</div>
  <div class="abs field area" style="top:815px">About your case...</div>
  <div class="abs btn" style="top:891px">Submit</div>

  <div class="abs tab tab-right" style="top:937px;padding-left:12px">Newsletter Sign-Up</div>
  <div class="abs field" style="top:973px">Name</div>
  <div class="abs field" style="top:995px">Email</div>
  <div class="abs btn" style="top:1023px">Subscribe</div>

  <footer class="abs footer">
    <div class="abs footer-links">Whitcombe Law<span>|</span>Contact Us<span>|</span>Resources<span>|</span>Privacy Policy<span>|</span>Site Map</div>
    <p class="abs footer-copy">Aliquam congue fermentum nisl. Mauris accumsan nulla vel diam. Sed in lacus ut enim adipiscing aliquet.<br>Praesent justo dolor, lobortis quis, lobortis dignissim, pulvinar ac, lorem.</p>
    <div class="abs footer-rule"></div>
    <div class="abs copyright">Copyright © 2012.&nbsp; Whitcombe Law.&nbsp; All Rights Reserved.</div>
    <div class="abs footer-brand"><i class="brand-mark"></i><span class="brand-name">Whitcombe Law</span></div>
    <div class="abs footer-phone">555.014.2863</div>
    <div class="abs footer-addr">48 Linden Court, Suite 310<br>Fairhaven, Ohio 4417.</div>
  </footer>
</div>
</body>
</html>
```